Brenner & Holloway Stationery

Greetings again. Now we've got an awesome logo, it's time to get the stationery to go with it. We require the following items of stationery:

- Business Card - Print Ready, all we need to do is change names and numbers and submit to printer.  Double sided with logo on one side and details on the other side. (85mm x 55mm)

- With Compliments Slip

- Letterhead - These will be preprinted pages that will then be used as pages.
(A4)

- Envelope - Business Size(Standard DL)

Target Market(s)

Essentially, this firm services clients facing criminal charges and/or seeking legal aid. The firm is also looking at taking on more white-collar crime cases.

Requirements
Must have
• - Same Design Cues & Colours as the Branding details attached

• - Address (as follows)

• Suite 8

• 262-268 Marlow St

• LARKVALE VIC 3184

• Phone: (03) 9482 6315

• Fax: (03) 9482 6840

• Web: www.brennerandholloway.example.au

• - Colour: Pantone 194 (Red)

```html
<!DOCTYPE html>
<html lang="en">
<head>
<meta charset="utf-8">
<title>Brenner &amp; Holloway Stationery</title>
<link rel="stylesheet" href="https://fonts.googleapis.com/css2?family=Cormorant+Garamond:ital,wght@0,500;0,600;1,600&family=Source+Sans+3:wght@400;600&display=swap">
<style>
  :root {
    --brand: #8e1f3f;
    --ink: #3a3a3a;
    --rule: #b5b5b5;
    --paper: #ffffff;
    --stage: #000000;
    --edge: #9a9a9a;
  }
  * { box-sizing: border-box; margin: 0; padding: 0; }
  html, body { width: 1200px; height: 982px; overflow: hidden; background: var(--stage); }
  .canvas { position: relative; width: 1200px; height: 982px; background: var(--stage); }
  .sheet { position: absolute; background: var(--paper); }
  .sheet--outlined { border: 1px solid var(--edge); }

  .letterhead { left: 59px; top: 26px; width: 656px; height: 930px; }
  .envelope { left: 301px; top: 198px; width: 846px; height: 411px; }
  .comp-slip { left: 559px; top: 427px; width: 379px; height: 246px; }
  .business-card { left: 765px; top: 706px; width: 380px; height: 247px; }

  .brand-lockup { position: absolute; display: flex; align-items: center; }
  .brand-lockup__dot { width: 58px; height: 58px; border-radius: 50%; background: var(--brand); flex: none; }
  .brand-lockup__rule { width: 1px; height: 46px; background: var(--rule); margin: 0 10px; flex: none; }
  .brand-lockup__name {
    font-family: "Cormorant Garamond", Georgia, serif;
    font-weight: 600; font-size: 20px; letter-spacing: 0.4px; line-height: 1;
    font-variant: small-caps; color: var(--brand); white-space: nowrap;
    margin-top: -10px;
  }
  .letterhead .brand-lockup { left: 208px; top: 47px; }
  .envelope .brand-lockup { left: 38px; top: 40px; }
  .comp-slip .brand-lockup { left: 79px; top: 84px; }

  .return-address {
    position: absolute; left: 122px; top: 100px;
    font-family: "Cormorant Garamond", Georgia, serif; font-style: normal;
    font-weight: 500; font-size: 13px; line-height: 17px; color: var(--ink);
  }

  .letterhead__footer {
    position: absolute; left: 45px; bottom: 21px;
    font-family: "Cormorant Garamond", Georgia, serif;
    font-weight: 500; font-size: 9.5px; color: var(--ink); white-space: nowrap;
  }
  .sep { padding: 0 6px; color: #888; }

  .card-details { position: absolute; left: 29px; top: 128px; }
  .card-details__name {
    font-family: "Source Sans 3", Arial, sans-serif; font-weight: 600;
    font-size: 14px; letter-spacing: 0.6px; color: var(--brand); text-transform: uppercase;
  }
  .card-details__role {
    font-family: "Cormorant Garamond", Georgia, serif; font-style: italic; font-weight: 600;
    font-size: 13px; color: var(--ink); margin-bottom: 8px;
  }
  .card-details__line {
    font-family: "Cormorant Garamond", Georgia, serif; font-weight: 500;
    font-size: 13.5px; line-height: 17px; color: var(--ink); white-space: nowrap;
  }
  .card-details__web {
    font-family: "Source Sans 3", Arial, sans-serif; font-weight: 600;
    font-size: 13px; color: var(--brand); margin-top: 6px;
  }
</style>
</head>
<body>
<div class="canvas">

  <section class="sheet letterhead" aria-label="Letterhead">
    <div class="brand-lockup">
      <span class="brand-lockup__dot"></span>
      <span class="brand-lockup__rule"></span>
      <span class="brand-lockup__name">Brenner &amp; Holloway</span>
    </div>
    <p class="letterhead__footer">
      Suite 8<span class="sep">|</span>262-268 Marlow St<span class="sep">|</span>Larkvale Vic 3184<span class="sep">|</span>Phone (03) 9482-6315<span class="sep">|</span>Fax (03) 9482-6840<span class="sep">|</span>Web www.brennerandholloway.example.au
    </p>
  </section>

  <section class="sheet sheet--outlined envelope" aria-label="DL envelope">
    <div class="brand-lockup">
      <span class="brand-lockup__dot"></span>
      <span class="brand-lockup__rule"></span>
      <span class="brand-lockup__name">Brenner &amp; Holloway</span>
    </div>
    <address class="return-address">
      Suite 8 | 262-268 Marlow St<br>
      Larkvale Vic 3184
    </address>
  </section>

  <section class="sheet sheet--outlined comp-slip" aria-label="With compliments slip">
    <div class="brand-lockup">
      <span class="brand-lockup__dot"></span>
      <span class="brand-lockup__rule"></span>
      <span class="brand-lockup__name">Brenner &amp; Holloway</span>
    </div>
  </section>

  <section class="sheet sheet--outlined business-card" aria-label="Business card, details side">
    <div class="card-details">
      <p class="card-details__name">Daniel Price</p>
      <p class="card-details__role">Corporate Attorney</p>
      <p class="card-details__line">Suite 8<span class="sep">|</span>262-268 Marlow St<span class="sep">|</span>Larkvale Vic 3184</p>
      <p class="card-details__line">Phone (03) 9482-6315<span class="sep">|</span>Fax (03) 9482-6840</p>
      <p class="card-details__web">www.brennerandholloway.example.au</p>
    </div>
  </section>

</div>
</body>
</html>
```